Informative 1-Pager website that informs users about the threat of ransomware

See current page: https://www.brixlo-vantel.com/

Coding

Coded - Design and coding required

```html
<!DOCTYPE html>
<html lang="en">
<head>
<meta charset="utf-8">
<title>Brixlo Vantel – Learn How To Protect Yourself From Ransomware</title>
<link href="https://fonts.googleapis.com/css2?family=IBM+Plex+Sans:wght@500;600;700&family=Poppins:wght@300;400;500;600;700&display=swap" rel="stylesheet">
<style>
  :root{
    --navy:#0b3050;
    --navy-deep:#082540;
    --yellow:#fdc230;
    --ink:#1d2b3a;
    --body:#3b4550;
    --muted:#e3e6ea;
    --line:#eceef1;
    --white:#ffffff;
  }
  *{margin:0;padding:0;box-sizing:border-box}
  html,body{width:1200px;height:4612px;overflow:hidden}
  body{position:relative;background:var(--white);font-family:"Poppins",sans-serif;color:var(--body)}
  .abs{position:absolute}
  .hl{color:var(--yellow)}
  .section-title{font-family:"IBM Plex Sans",sans-serif;font-weight:600;font-size:29px;line-height:38px;color:var(--ink)}
  .section-title .hl{font-weight:600}

  /* Hero */
  .hero{position:absolute;left:0;top:0;width:1200px;height:750px;
    background:radial-gradient(ellipse at 60% 40%,#124068 0%,var(--navy) 55%,var(--navy-deep) 100%)}
  .hero-pattern{position:absolute;left:130px;top:0;width:1070px;height:650px;
    background:linear-gradient(100deg,rgba(40,140,110,0) 0%,rgba(40,140,110,.16) 45%,rgba(40,140,110,.05) 80%)}
  .brand{position:absolute;left:161px;top:20px;font-family:"Poppins",sans-serif;font-size:30px;font-weight:600;color:var(--yellow)}
  .hero-title{position:absolute;z-index:2;left:161px;top:222px;width:460px;font-size:31px;line-height:40px;color:var(--white);font-weight:300;white-space:nowrap}
  .hero-title strong{display:block;color:var(--yellow);font-weight:600}
  .hero-text{position:absolute;z-index:2;left:161px;top:316px;width:390px;font-size:15px;line-height:25px;color:var(--white)}
  .btn{position:absolute;left:161px;top:390px;width:148px;height:36px;border-radius:18px;background:var(--yellow);
    color:var(--navy);font-size:14px;font-weight:500;text-align:center;line-height:36px}
  .hero-media{position:absolute;left:640px;top:176px;width:492px;height:311px;border-radius:10px;
    background:linear-gradient(160deg,#c9ccd1 0%,#e0654f 30%,#d2533f 60%,#b6bcc4 100%)}
  .wave{position:absolute;left:0;top:540px;width:1200px;height:212px}

  /* Nutshell */
  .nutshell-title{left:0;width:1200px;top:803px;text-align:center}
  .nutshell-text{left:270px;top:858px;width:660px;text-align:center;font-size:13.5px;line-height:24px}

  /* Types */
  .types-media{left:0;top:1012px;width:455px;height:525px;border-radius:0 14px 14px 0;
    background:linear-gradient(135deg,#3a3226 0%,#6b5640 35%,#1f3b35 65%,#141c1e 100%)}
  .types-badge{left:150px;top:1454px;width:158px;height:140px;border-radius:12px;
    background:linear-gradient(160deg,#3a7bd5 0%,#e0483e 55%,#0b3050 100%)}
  .types-faint{left:161px;top:1602px;font-size:24px;font-weight:600;color:var(--muted)}
  .types-head{left:491px;top:1006px}
  .types-intro{left:491px;top:1090px;font-size:14px;color:var(--body)}
  .type-list{left:455px;top:1148px;width:745px;border-top:1px solid var(--line);border-left:1px solid var(--line)}
  .type-row{position:relative;border-bottom:1px solid var(--line);padding:18px 164px 14px 136px}
  .type-row svg{position:absolute;left:40px;top:50%;transform:translateY(-50%);width:56px;height:56px}
  .type-row h3{font-family:"Poppins",sans-serif;font-size:16px;font-weight:600;color:var(--ink);line-height:22px;margin-bottom:5px}
  .type-row p{font-size:12.5px;line-height:21.5px;text-align:justify}

  /* Dark section */
  .dark{position:absolute;left:0;top:2043px;width:1200px;height:864px;background:var(--navy)}
  .dark-media{left:257px;top:1805px;width:686px;height:300px;border-radius:12px;background:var(--white);padding:7px}
  .dark-media div{width:100%;height:100%;border-radius:8px;
    background:linear-gradient(110deg,#1e2a35 0%,#3c5a73 40%,#5f9fc9 70%,#2e4c66 100%)}
  .dark-title{left:0;width:1200px;top:2142px;text-align:center;color:var(--white)}
  .dark p{position:absolute;font-size:12.4px;line-height:21.6px;color:var(--white);text-align:justify}
  .dark .col-a{left:163px;width:419px}
  .dark .col-b{left:618px;width:419px}
  .dark .full{left:163px;width:874px}
  .dark .cta{left:0;width:1200px;text-align:center;font-weight:600;font-size:13px}

  /* Features */
  .feature-title{left:161px}
  .feature-text{font-size:14px;line-height:24.5px;letter-spacing:.5px;text-align:justify;width:414px}
  .feature-text p+p{margin-top:12px}
  .feature-media{width:410px;height:410px;border-radius:14px}

  /* Footer */
  .footer{position:absolute;left:0;top:4474px;width:1200px;height:138px;background:var(--navy)}
  .footer-brand{position:absolute;left:161px;top:20px;font-family:"IBM Plex Sans",sans-serif;font-weight:600;font-size:29px;color:var(--white)}
  .follow{position:absolute;left:878px;top:37px;font-size:11px;color:var(--white)}
  .social{position:absolute;top:29px;width:29px;height:29px;border-radius:3px;background:var(--yellow)}
  .copyright{position:absolute;left:0;width:1200px;top:106px;text-align:center;font-size:11px;color:var(--white)}
</style>
</head>
<body>

<header class="hero">
  <div class="hero-pattern" role="img" aria-label="Faint green binary code pattern"></div>
  <div class="brand">Brixlo Vantel</div>
  <div class="hero-media" role="img" aria-label="Laptop showing a ransomware attack warning screen"></div>
  <h1 class="hero-title">Learn How To Protect <strong>Yourself From Ransomware</strong></h1>
  <p class="hero-text">Keep your computer safe and understand how to act in case of an successful attack</p>
  <div class="btn">Contact Us</div>
  <svg class="wave" viewBox="0 0 1200 212" preserveAspectRatio="none" aria-hidden="true">
    <path d="M0,40 C250,5 420,160 700,168 C900,174 1060,108 1200,68 L1200,212 L0,212 Z" fill="var(--yellow)"/>
    <path d="M0,60 C250,30 400,188 700,198 C900,204 1060,150 1200,92 L1200,212 L0,212 Z" fill="var(--white)"/>
  </svg>
</header>

<h2 class="abs section-title nutshell-title">Ransomware In A <span class="hl">Nutshell</span></h2>
<p class="abs nutshell-text">Ransomware is a very dangerous cyber threat to all organisations and individuals. Ransomware is a type of malicious software that may block access to files or devices until the victim pays a ransom.The ransom is usually demanded in cryptocurrency.</p>

<div class="abs types-media" role="img" aria-label="Hacker working at computer screens in a dark room"></div>
<div class="abs types-badge" role="img" aria-label="Illustration of a phone with padlock and shield"></div>
<div class="abs types-faint">Brixlo Vantel</div>

<h2 class="abs section-title types-head">What Are<br><span class="hl">Common Ransomware Types?</span></h2>
<p class="abs types-intro">There are many different types of ransomware. Here are four typical categories:</p>

<div class="abs type-list">
  <div class="type-row" style="height:147px">
    <svg viewBox="0 0 56 56" fill="none" stroke="var(--ink)" stroke-width="2.2" stroke-linejoin="round"><path d="M28 10 L50 46 H6 Z"/><line x1="28" y1="22" x2="28" y2="35" stroke-linecap="round"/><circle cx="28" cy="40" r="1.6" fill="var(--ink)"/></svg>
    <h3>Ransomware That Fakes Something</h3>
    <p>Scareware fakes a problem on the computer. For example, it could be a warning that a virus or malware has been found on the PC. The software then redirects the user to a website where the problem can be solved for a fee.</p>
  </div>
  <div class="type-row" style="height:122px">
    <svg viewBox="0 0 56 56" fill="none" stroke="var(--ink)" stroke-width="2"><circle cx="28" cy="28" r="13"/><circle cx="28" cy="28" r="5" fill="var(--yellow)"/><path d="M28 6v8M28 42v8M6 28h8M42 28h8M13 13l5 5M38 38l5 5M43 13l-5 5M18 38l-5 5"/></svg>
    <h3>Ransomware That Encrypts Something</h3>
    <p>Encryptors are the most common type of ransomware that encrypts all data and requires a key to unlock it, which can usually be purchased within a short period of time.</p>
  </div>
  <div class="type-row" style="height:122px">
    <svg viewBox="0 0 56 56" fill="none" stroke="var(--ink)" stroke-width="2"><rect x="12" y="14" width="26" height="34" rx="3"/><rect x="18" y="30" width="12" height="10" rx="1.5" fill="var(--yellow)"/><path d="M20 30v-4a4 4 0 0 1 8 0v4"/><path d="M42 8h6v6M46 20h4M40 16h4"/></svg>
    <h3>Ransomware That Leaks Data</h3>
    <p>This type of ransomware is called Doxware. Doxware often tries to force the user or the company to pay by threatening to publish confidential information online at a "Hall of Shame".</p>
  </div>
  <div class="type-row" style="height:170px">
    <svg viewBox="0 0 56 56" fill="none" stroke="var(--ink)" stroke-width="2"><rect x="10" y="12" width="36" height="24" rx="2"/><path d="M6 42h44"/><rect x="23" y="23" width="10" height="8" rx="1.5" fill="var(--yellow)"/><path d="M25 23v-3a3 3 0 0 1 6 0v3"/></svg>
    <h3>Ransomware That Locks Something</h3>
    <p>Instead of preventing access to files or applications, this ransomware type prevent the end user's device from being used. For example, key combinations (CTRL+ALT+DEL) are also locked, so that the user can no longer access his current work. Usually, details of the ransomware are displayed on the lock screen.</p>
  </div>
</div>

<section class="dark">
  <p class="col-a" style="top:173px">If one does not pay the ransom and has no backup, the data is usually lost forever. Sometimes, however, the data ends up on the dark web and the affected companies are exposed. Thus, it is not the loss of the data that is the angle with which the hackers build up pressure, but the reputation damage caused by the lost data. This damage can be much greater than the value of the individual data. For example, who wants to do business with a bank that can't even protect itself? Every potential customer will not weigh his own money in security and go to a competitor.</p>
  <p class="col-b" style="top:173px">In the darknet, some hacker collectives operate websites where the attacked companies are exposed at a "hall of shame". This is where the complete data sets are published for everyone to see. By using free download links, all data can then also be downloaded immediately. Often, these data sets contain personal information about employees. Such a violation of privacy due to insufficient protection can lead to high penalties due to legal requirements such as GDPR. But unfortunately, the data leaks also often affect customers and partners of the involved organization, depending on the position of the employee who was hacked.</p>
  <p class="full" style="top:413px">The hackers are of course aware of the explosive nature of such revelations and have no scruples about making their threats come true. The Norvett research team (https://www.norvett.io) has recently noticed an accumulation of such activity on the dark web. A recent example was the Kr4ken ransomware group. After ceasing all operations for several months between November 21 and February 22, the Kr4ken group was now active again. The increase in activity was noticed after the ransomware group added 21 new victims to its data leak site in a single month in April. Kr4ken has become very active compared to the past. Comparison with other ransomware groups in April: Vaultbyte 2.0 published 103 victims and Morvo – 45 victims, Kr4ken's victims have increased massively, from 1 to 21. The industrial sector was Kr4ken's main target: 45% of Kr4ken ransomware attacks affected industrial companies and 27% targeted technology companies. Companies that know which sectors the ransomware group attacks most often should consider the possibility of being the next target of this gang and prepare accordingly.</p>
  <p class="col-a" style="top:614px">The list of companies whose servers have been hacked by Kr4ken in the past includes energy giant Harlow Energy, cybersecurity company Vexant, supermarket giant Greenmart, and several universities around the world (the University of Eastvale, the University of Southport, Redwood Medicine, the University of Northfield Baltimore (UNB), and the University of Westmark).</p>
  <p class="col-b" style="top:614px">The victims of such security breaches naturally learn before the public does. Suppliers and partners, however, usually remain in the dark. Therefore, it is important to monitor the Dark Web and all common ransomware groups. The most important business relationships should be included in the monitoring plan, and the focus should not only be on the company's own organization.</p>
  <p class="cta" style="top:764px">Norvett Offers A Range of Unique Dark Web Ad Ransomware Monitoring Services To Mitigate Those Risks.</p>
</section>
<div class="abs dark-media"><div role="img" aria-label="Hooded hacker beside a glowing digital dollar sign"></div></div>
<h2 class="abs section-title dark-title">What If You <span class="hl">Don't Pay</span> The Ransom?</h2>

<h2 class="abs section-title feature-title" style="top:3050px">How Can You Get<br><span class="hl">Infected By Ransomware?</span></h2>
<div class="abs feature-text" style="left:161px;top:3153px">
  <p>Lorem ipsum dolor sit amet, consectetuer adipiscing elit. Donec odio. Quisque volutpat mattis eros. Nullam malesuada erat ut turpis. Suspendisse urna nibh, viverra non, semper suscipit, posuere a, pede.</p>
  <p>Lorem ipsum dolor sit amet, consectetuer adipiscing elit. Donec odio. Quisque volutpat mattis eros. Nullam malesuada erat ut turpis.</p>
</div>
<div class="abs feature-media" style="left:627px;top:2989px;background:linear-gradient(135deg,#1b2f7a 0%,#3a6fd0 40%,#c23a8a 70%,#23c0d8 100%)" role="img" aria-label="Screen with a red malware warning sign"></div>

<div class="abs feature-media" style="left:161px;top:3484px;background:linear-gradient(135deg,#e9e4dc 0%,#b9a48a 35%,#2a4f8f 65%,#d9d5cf 100%)" role="img" aria-label="Person at a computer showing a protected padlock screen"></div>
<h2 class="abs section-title" style="left:623px;top:3547px">How Can You Avoid<br><span class="hl">A Ransomware Attack?</span></h2>
<div class="abs feature-text" style="left:623px;top:3650px">
  <p>Lorem ipsum dolor sit amet, consectetuer adipiscing elit. Donec odio. Quisque volutpat mattis eros. Nullam malesuada erat ut turpis. Suspendisse urna nibh, viverra non, semper suscipit, posuere a, pede.</p>
  <p>Lorem ipsum dolor sit amet, consectetuer adipiscing elit. Donec odio. Quisque volutpat mattis eros. Nullam malesuada erat ut turpis.</p>
</div>

<h2 class="abs section-title feature-title" style="top:4041px">How Can You Get<br><span class="hl">Infected By Ransomware?</span></h2>
<div class="abs feature-text" style="left:161px;top:4144px">
  <p>Lorem ipsum dolor sit amet, consectetuer adipiscing elit. Donec odio. Quisque volutpat mattis eros. Nullam malesuada erat ut turpis. Suspendisse urna nibh, viverra non, semper suscipit, posuere a, pede.</p>
  <p>Lorem ipsum dolor sit amet, consectetuer adipiscing elit. Donec odio. Quisque volutpat mattis eros. Nullam malesuada erat ut turpis.</p>
</div>
<div class="abs feature-media" style="left:627px;top:3982px;background:radial-gradient(ellipse at 55% 45%,#6f8a5a 0%,#2b3324 35%,#0d0f0c 75%)" role="img" aria-label="Hacker typing on laptops in a dark room"></div>

<footer class="footer">
  <div class="footer-brand">Brixlo Vantel</div>
  <div class="follow">Follow Us On :</div>
  <div class="social" style="left:972px" role="img" aria-label="Social network link"></div>
  <div class="social" style="left:1008px" role="img" aria-label="Social network link"></div>
  <div class="copyright">© 2022 Brixlo Vantel. All Rights Reserved.</div>
</footer>

</body>
</html>
```